Loft Plan Studio New Business Card

I am opening a new division of my business. I am a high end interior designer, and the new business is writing specs for construction projects. It will be marketed to the VERY high end contractor, architects and realtors. The client will actually be the one who pays us and signs the agreement, but it will be the contractor, architect or realtor that will recommend us. I have attached my current card and our previous logo which is still used on some of our paperwork. I would like the new logo to be connected in some way to what we are currently using. We will need to have room on the card for a person's name. I'd like to omit the address as we might be moving the office soon. The web address is www.LoftPlanStudio.example. For this design, please use my name, Marisol Whitfield.

Target Market(s)

High End Luxury Contractors, Realtors and Architects

Industry/Entity Type

Residential Construction

Contact Information for Business Card

Loft Plan Studio, Phone: 555-304-2917, www.LoftPlanStudio.example , Marisol Whitfield

Font styles to use
Sans Serif

Colors
ec1f27

Requirements
Must have
• Some visual reference to my current card and logos. Use the colors submitted on the business card I attached.
Nice to have
• A visual reference to my current card and logos. Use the colors submitted on the card I attached.
Should not have
• A physical address

```html
<!DOCTYPE html>
<html lang="en">
<head>
<meta charset="utf-8">
<title>Loft Plan Studio – Business Card</title>
<link rel="stylesheet" href="https://fonts.googleapis.com/css2?family=Didact+Gothic&family=PT+Sans:wght@400;700&display=swap">
<style>
  :root {
    --stage: #000000;
    --card: #ffffff;
    --brand-brown: #8a3100;
    --text-gray: #7a7a7a;
    --rule-gray: #808080;
  }
  * { margin: 0; padding: 0; box-sizing: border-box; }
  html, body {
    width: 1200px;
    height: 1000px;
    overflow: hidden;
    background: var(--stage);
  }
  .canvas {
    position: relative;
    width: 1200px;
    height: 1000px;
    background: var(--stage);
  }
  .card {
    position: absolute;
    left: 258px;
    width: 683px;
    height: 391px;
    background: var(--card);
    overflow: hidden;
  }
  .card--front { top: 86px; }
  .card--back  { top: 518px; height: 390px; }

  /* Front */
  .brand-square {
    position: absolute;
    left: 275px;
    top: 89px;
    width: 135px;
    height: 123px;
    background: var(--brand-brown);
  }
  .brand-name {
    position: absolute;
    left: 0;
    top: 226px;
    width: 100%;
    text-align: center;
    font-family: "Didact Gothic", sans-serif;
    font-size: 50px;
    line-height: 60px;
    letter-spacing: 1px;
    color: var(--text-gray);
  }

  /* Back */
  .contact {
    position: absolute;
    left: 0;
    width: 100%;
    text-align: center;
    font-family: "PT Sans", sans-serif;
    color: var(--text-gray);
  }
  .person-name {
    top: 114px;
    font-size: 35px;
    line-height: 44px;
    color: var(--brand-brown);
  }
  .phones {
    top: 170px;
    font-size: 20px;
    line-height: 25px;
    font-weight: 700;
  }
  .phones .label { color: var(--brand-brown); }
  .website {
    top: 232px;
    font-size: 19px;
    line-height: 24px;
    font-weight: 700;
  }
  .tagline {
    top: 338px;
    font-size: 20px;
    line-height: 26px;
    font-weight: 700;
  }
</style>
</head>
<body>
<main class="canvas">
  <section class="card card--front" aria-label="Card front">
    <div class="brand-square"></div>
    <h1 class="brand-name">Loft Plan Studio</h1>
  </section>

  <section class="card card--back" aria-label="Card back">
    <p class="contact person-name">Marisol Whitfield</p>
    <p class="contact phones">
      <span class="label">Office:</span> 555.304.2917<br>
      <span class="label">Cell:</span> 555.304.6148
    </p>
    <p class="contact website">www.LoftPlanStudio.example</p>
    <p class="contact tagline">Professional Specifications for Contractors</p>
  </section>
</main>
</body>
</html>
```